Qb Panes

We need a website design for a company based in Texas that specializes in doors and and windows.
Qb Pane is a leading window manufacturer of aluminum and vinyl windows, both serving the replacement and new construction markets. Qb Pane Inc. was created over 25 years ago when two existing window manufacturers with excellent reputations in their fields - merged. Qb Pane offers a complete line conforming to the needs of residential and commercial window markets.
The final design should be something that communicates professionalism and features they're key value propositions.
Example websites we like:
http://layouts.pebblecraft.example/zx/satchel/
http://layouts.pebblecraft.example/zx/splashyard/
http://layouts.pebblecraft.example/zx/rebuildr2/
This design should format the existing content to be more visually organized, improve the fonts to clearer and more readable, and make it easier for users to find services.
Brand guide is attached
Website images can be found here: https://docs.vaultcrate.example/7kRTmwQzLpXeBd
Target Market(s)
Windows
Number of Pages Required
1 page
Look and feel
Each slider illustrates characteristics of the customer's brand and the style your logo design should communicate.

```html
<!DOCTYPE html>
<html lang="en">
<head>
<meta charset="utf-8">
<title>Qb Pane — Windows &amp; Doors</title>
<link href="https://fonts.googleapis.com/css2?family=Dosis:wght@400;500;600;700&family=Playfair+Display:wght@400&display=swap" rel="stylesheet">
<style>
:root{
  --gold:#e8b931;
  --gold-dark:#d7a520;
  --crimson:#9b1b3a;
  --ink:#2d2a26;
  --grey:#8a8580;
  --light:#f4f3f1;
  --dark:#2a2521;
  --white:#ffffff;
}
*{box-sizing:border-box;margin:0;padding:0}
html,body{width:1200px;height:3600px;overflow:hidden}
body{font-family:'Dosis',sans-serif;color:var(--ink);background:var(--white);position:relative}
.abs{position:absolute}
.topbar{top:0;left:0;width:1200px;height:48px;background:var(--gold);color:var(--white)}
.topbar .phone{left:72px;top:12px;font-size:22px;font-weight:500;display:flex;align-items:center;gap:10px}
.topbar .social{right:72px;top:16px;display:flex;gap:18px}
.topbar .social span{width:14px;height:14px;border-radius:50%;background:var(--white)}
.nav{top:48px;left:0;width:1200px;height:80px;background:var(--white);box-shadow:0 2px 6px rgba(0,0,0,.08)}
.nav a{position:absolute;top:44px;font-size:13px;font-weight:600;color:var(--crimson);text-decoration:none;letter-spacing:.5px}
.brand{left:480px;top:56px;width:240px;text-align:center;font-family:'Dosis',sans-serif;font-size:38px;font-weight:600;color:var(--crimson);line-height:1}
.hero{top:128px;left:0;width:1200px;height:501px;background:linear-gradient(100deg,#3b3a36 0%,#8a7648 35%,#e6cf86 60%,#b89556 80%,#4a3a2a 100%)}
.hero-box{top:257px;left:0;width:516px;height:223px;background:rgba(35,30,25,.78);padding:60px 0 0 72px}
.hero-box .pre{font-size:28px;font-weight:600;color:var(--white)}
.hero-box .big{font-size:46px;font-weight:700;color:var(--gold);letter-spacing:2px;margin-top:4px}
.arrow{width:43px;height:43px;background:var(--gold);display:flex;align-items:center;justify-content:center}
.arrow.dark{background:#333}
.infoband{top:629px;left:0;width:1200px;height:134px;background:var(--gold);color:var(--white)}
.info{top:40px;display:flex;align-items:center;gap:18px;font-size:15px;font-weight:600;line-height:1.4}
.info .ic{width:54px;height:54px;border-radius:50%;background:var(--white);display:flex;align-items:center;justify-content:center;flex:none}
.about-img{top:763px;left:0;width:581px;height:387px;background:linear-gradient(135deg,#d9c9a8 0%,#9c6a3c 45%,#6a4225 100%)}
.about{top:763px;left:581px;width:619px;height:387px;background:var(--light);padding:50px 60px 0 34px}
.h2{font-size:40px;font-weight:500;color:var(--crimson);letter-spacing:1px}
.rule{position:relative;height:2px;width:160px;background:var(--crimson);opacity:.5;margin-top:6px}
.rule::after{content:"";position:absolute;left:50%;top:-3px;width:8px;height:8px;margin-left:-4px;border-radius:50%;background:var(--crimson)}
.about p{font-size:15px;line-height:1.6;color:var(--grey);margin-top:18px}
.btn{display:inline-block;background:var(--gold);color:var(--white);font-weight:600;font-size:15px;border-radius:20px;padding:8px 30px;letter-spacing:.5px}
.sec-title{left:0;width:1200px;text-align:center}
.sec-title .rule{margin:6px auto 0}
.svc-img{top:1279px;left:456px;width:288px;height:394px;background:linear-gradient(180deg,#c5cfd6 0%,#6b6e72 45%,#4f7d3c 85%,#5f9244 100%);box-shadow:0 4px 12px rgba(0,0,0,.25)}
.svc-ic{width:96px;height:96px;border-radius:50%;background:var(--gold);border:4px solid #f3dc97;display:flex;align-items:center;justify-content:center}
.svc-text{width:250px;font-size:15px;line-height:1.5;color:var(--grey)}
.style-sec{top:1733px;left:0;width:1200px;height:734px;background:linear-gradient(180deg,#efefef,#fafafa 60%,#ececec)}
.tabs{top:1895px;left:0;width:1200px;text-align:center;font-size:15px;font-weight:600}
.grid{top:1934px;left:72px;width:1056px;height:410px;display:grid;grid-template-columns:repeat(4,1fr);grid-template-rows:repeat(2,1fr)}
.grid div{position:relative}
.grid .cap{position:absolute;left:0;right:0;top:140px;height:50px;background:rgba(255,255,255,.8);text-align:center;line-height:50px;font-size:15px;color:var(--ink);letter-spacing:.5px}
.testi{top:2467px;left:0;width:1200px;height:329px;background:linear-gradient(180deg,#2e2824,#4a3527 60%,#2a2420)}
.photo{top:2585px;left:72px;width:156px;height:151px;background:linear-gradient(160deg,#d8d6d2,#9a8b80);border:3px solid var(--white)}
.testi .name{left:252px;top:2583px;font-size:22px;font-weight:700;color:var(--gold);letter-spacing:1px}
.testi .role{left:252px;top:2608px;font-size:15px;color:var(--white)}
.testi .quote{left:252px;top:2640px;width:870px;font-size:15px;line-height:1.6;color:#e8e4df}
.news-img{top:2914px;width:516px;height:182px}
.news-date{top:3112px;font-size:15px;font-weight:600;color:var(--crimson)}
.news-text{top:3142px;width:516px;font-size:15px;line-height:1.6;color:var(--grey)}
.news-text b{color:var(--crimson)}
.footer{top:3276px;left:0;width:1200px;height:276px;background:linear-gradient(180deg,#2b2622,#3a322b)}
.footer h4{font-size:14px;font-weight:700;color:var(--gold);letter-spacing:.5px}
.footer ul{list-style:none;margin-top:12px}
.footer li{font-size:13px;color:#ddd;margin-bottom:14px;letter-spacing:.5px}
.fcontact div{display:flex;gap:12px;align-items:flex-start;font-size:12px;color:#ddd;line-height:1.6;margin-top:8px}
.fbrand{top:3366px;left:862px;width:266px;text-align:center;font-size:40px;font-weight:600;color:var(--white)}
.fsocial{top:3428px;left:884px;display:flex;gap:14px}
.fsocial span{width:24px;height:24px;background:#1e6fd0}
.fsocial span.r{background:#d43c2c}
.copy{top:3552px;left:0;width:1200px;height:48px;background:var(--gold);color:var(--white);text-align:center;line-height:48px;font-size:14px;font-weight:500}
.totop{right:14px;top:3538px;width:30px;height:30px;background:#333;display:flex;align-items:center;justify-content:center}
</style>
</head>
<body>

<header class="abs topbar">
  <div class="abs phone">
    <svg width="18" height="18" viewBox="0 0 24 24"><path fill="#fff" d="M6.6 10.8a15 15 0 0 0 6.6 6.6l2.2-2.2c.3-.3.7-.4 1-.2 1.1.4 2.3.6 3.6.6.6 0 1 .4 1 1V20c0 .6-.4 1-1 1A17 17 0 0 1 3 4c0-.6.4-1 1-1h3.5c.6 0 1 .4 1 1 0 1.3.2 2.5.6 3.6.1.3 0 .7-.2 1z"/></svg>
    555.014.2290
  </div>
  <div class="abs social"><span></span><span></span><span></span><span></span><span></span></div>
</header>

<nav class="abs nav">
  <a style="left:188px">HOME</a>
  <a style="left:266px">ABOUT US</a>
  <a style="left:370px">SERVICES</a>
  <a style="left:770px">NEWS</a>
  <a style="left:852px">TESTIMONIAL</a>
  <a style="left:972px">CONTACT US</a>
</nav>
<div class="abs brand">Qb Pane</div>

<section class="abs hero" role="img" aria-label="Photo of a warmly lit modern living room with floor-to-ceiling sliding glass doors at dusk"></section>
<div class="abs hero-box">
  <div class="pre">We Probide Highest Quality</div>
  <div class="big">SERVICES</div>
</div>
<div class="abs arrow" style="left:0;top:356px"><svg width="14" height="18" viewBox="0 0 14 18"><path d="M10 2 3 9l7 7" stroke="#fff" stroke-width="3" fill="none"/></svg></div>
<div class="abs arrow dark" style="right:0;top:356px"><svg width="14" height="18" viewBox="0 0 14 18"><path d="m4 2 7 7-7 7" stroke="#fff" stroke-width="3" fill="none"/></svg></div>
<svg class="abs" style="left:590px;top:598px" width="20" height="20" viewBox="0 0 20 20"><path d="m4 3 6 6 6-6M4 10l6 6 6-6" stroke="#fff" stroke-width="2" fill="none"/></svg>

<section class="abs infoband">
  <div class="abs info" style="left:106px">
    <span class="ic"><svg width="22" height="26" viewBox="0 0 24 28"><path fill="#e8b931" d="M12 0a10 10 0 0 0-10 10c0 7.5 10 18 10 18s10-10.5 10-18A10 10 0 0 0 12 0zm0 14a4 4 0 1 1 0-8 4 4 0 0 1 0 8z"/></svg></span>
    <span>lorem Ipsum is simply dummy<br>text of the printing and</span>
  </div>
  <div class="abs info" style="left:540px">
    <span class="ic"><svg width="24" height="24" viewBox="0 0 24 24"><path fill="#e8b931" d="M6.6 10.8a15 15 0 0 0 6.6 6.6l2.2-2.2c.3-.3.7-.4 1-.2 1.1.4 2.3.6 3.6.6.6 0 1 .4 1 1V20c0 .6-.4 1-1 1A17 17 0 0 1 3 4c0-.6.4-1 1-1h3.5c.6 0 1 .4 1 1 0 1.3.2 2.5.6 3.6.1.3 0 .7-.2 1z"/></svg></span>
    <span>555.014.2290</span>
  </div>
  <div class="abs info" style="left:878px">
    <span class="ic"><svg width="24" height="18" viewBox="0 0 24 18"><rect width="24" height="18" rx="2" fill="#e8b931"/><path d="m2 3 10 7 10-7" stroke="#fff" stroke-width="2" fill="none"/></svg></span>
    <span>info@qbpane.example</span>
  </div>
</section>

<div class="abs about-img" role="img" aria-label="Photo of a bright kitchen with wooden cabinets and a large window overlooking the sea"></div>
<section class="abs about">
  <h2 class="h2">ABOUT US</h2>
  <div class="rule"></div>
  <p>Lorem Ipsum is simply dummy text of the printing and typesetting industry. Lorem Ipsum has been the industry's standard dummy text ever since the 1500s, when an unknown printer took a galley of type and scrambled it to make a type specimen book. It has survived not only five centuries, but also the leap into electronic typesetting, remaining essentially unchanged. It was popularised in the 1960s with the release</p>
  <div class="btn" style="margin-top:22px">READ MORE</div>
</section>

<div class="abs sec-title" style="top:1198px"><h2 class="h2">OUR SERVICES</h2><div class="rule"></div></div>
<div class="abs svc-img" role="img" aria-label="Photo of a modern two-storey house with dark cladding and large windows"></div>

<div class="abs svc-text" style="left:74px;top:1392px;text-align:right">Lorem Ipsum is simply dummy text of the printing and typesetting</div>
<div class="abs svc-ic" style="left:331px;top:1368px"><svg width="44" height="44" viewBox="0 0 44 44" fill="none" stroke="#fff" stroke-width="2.5"><rect x="6" y="6" width="32" height="32"/><path d="M6 14h32M6 22h32M6 30h32"/></svg></div>
<div class="abs svc-text" style="left:74px;top:1541px;text-align:right">Lorem Ipsum is simply dummy text of the printing and typesetting</div>
<div class="abs svc-ic" style="left:331px;top:1517px"><svg width="44" height="44" viewBox="0 0 44 44" fill="none" stroke="#fff" stroke-width="2.5"><rect x="8" y="6" width="28" height="32"/><path d="M8 6c6 10 6 22 0 32M36 6c-6 10-6 22 0 32"/></svg></div>
<div class="abs svc-ic" style="left:773px;top:1368px"><svg width="44" height="44" viewBox="0 0 44 44" fill="none" stroke="#fff" stroke-width="2.5"><path d="M10 38V18a12 12 0 0 1 24 0v20z"/><path d="M22 6v32M10 22h24M10 30h24"/></svg></div>
<div class="abs svc-text" style="left:878px;top:1392px">Lorem Ipsum is simply dummy text of the printing and typesetting</div>
<div class="abs svc-ic" style="left:773px;top:1517px"><svg width="44" height="44" viewBox="0 0 44 44" fill="none" stroke="#fff" stroke-width="2.5"><rect x="6" y="6" width="32" height="32"/><path d="M22 6v32M6 18h32M10 22l8 8M34 22l-8 8"/></svg></div>
<div class="abs svc-text" style="left:878px;top:1541px">Lorem Ipsum is simply dummy text of the printing and typesetting</div>

<section class="abs style-sec"></section>
<div class="abs sec-title" style="top:1782px"><h2 class="h2">CHOOSE YOUR STYLE</h2><div class="rule"></div></div>
<div class="abs sec-title" style="top:1850px;font-size:16px;color:var(--ink)">Lorem Ipsum is simply dummy text of the printing and typesetting</div>
<div class="abs tabs"><span style="color:var(--crimson)">RESIDENCIAL</span>&nbsp;&nbsp;&nbsp;|&nbsp;&nbsp;&nbsp;<span>COMMERCIAL</span></div>
<div class="abs grid">
  <div role="img" aria-label="Photo of a white sunroom addition with many windows" style="background:linear-gradient(180deg,#c9d3da,#eef0ee 60%,#7d9a58)"></div>
  <div role="img" aria-label="Photo of a pergola over a patio with garden windows" style="background:linear-gradient(180deg,#6d5a48,#a89c88)"><div class="cap">LOREM IPSUM IS SIMPLY DUMMY</div></div>
  <div role="img" aria-label="Photo of a bright white living room with tall windows" style="background:linear-gradient(180deg,#f3f1ec,#d8d2c6)"></div>
  <div role="img" aria-label="Photo of a brick house with a bay window" style="background:linear-gradient(180deg,#6b4d3d,#3d3a38 70%,#8aa2b8)"></div>
  <div role="img" aria-label="Photo of a cream kitchen with a window above the sink" style="background:linear-gradient(180deg,#e6dcc0,#b8a27a)"></div>
  <div role="img" aria-label="Photo of a kitchen with a wide window and wooden cabinets" style="background:linear-gradient(180deg,#8b8a7e,#4b463e)"></div>
  <div role="img" aria-label="Photo of a dining room with windows overlooking water" style="background:linear-gradient(180deg,#a9bfcf,#6b5e52)"></div>
  <div role="img" aria-label="Photo of a green-walled kitchen with white cabinets" style="background:linear-gradient(180deg,#c8c7a6,#f0ede4 70%,#8b6a4a)"></div>
</div>
<div class="abs" style="left:528px;top:2369px;width:144px;text-align:center"><span class="btn" style="padding:8px 26px">VIEW ALL</span></div>

<section class="abs testi" role="img" aria-label="Dimmed photo of a kitchen interior as section background"></section>
<div class="abs sec-title" style="top:2512px"><h2 class="h2" style="color:var(--gold)">TESTIMONIAL</h2><div class="rule" style="background:var(--gold)"></div></div>
<div class="abs photo" role="img" aria-label="Portrait photo of the reviewing customer"></div>
<div class="abs name" style="left:252px;top:2583px;font-size:22px;font-weight:700;color:var(--gold);letter-spacing:1px">SAM RIVERA</div>
<div class="abs" style="left:252px;top:2610px;font-size:15px;color:var(--white)">Lorem Ipsum is simply</div>
<p class="abs" style="left:252px;top:2640px;width:870px;font-size:15px;line-height:1.6;color:#e8e4df">orem Ipsum is simply dummy text of the printing and typesetting industry. Lorem Ipsum has been the industry's standard dummy text ever since the 1500s, when an unknown printer took a galley of type and scrambled it to make a type specimen book. It has survived not only five centuries, but also the leap into electronic typesetting, remaining essentially unchanged. It was popularised in the 1960s with the release</p>
<div class="abs arrow" style="left:0;top:2640px"><svg width="14" height="18" viewBox="0 0 14 18"><path d="M10 2 3 9l7 7" stroke="#fff" stroke-width="3" fill="none"/></svg></div>
<div class="abs arrow" style="right:0;top:2640px"><svg width="14" height="18" viewBox="0 0 14 18"><path d="m4 2 7 7-7 7" stroke="#fff" stroke-width="3" fill="none"/></svg></div>

<div class="abs sec-title" style="top:2842px"><h2 class="h2">NEWS</h2><div class="rule" style="width:60px"></div></div>
<div class="abs news-img" style="left:72px;background:linear-gradient(120deg,#8fae6a,#e8ddc2 45%,#a0704a)" role="img" aria-label="Photo of a sunroom with wooden ceiling and garden views"></div>
<div class="abs news-img" style="left:612px;background:linear-gradient(120deg,#8f9aa2,#ebe6dc 50%,#b58a52)" role="img" aria-label="Photo of an open-plan living room and kitchen"></div>
<div class="abs news-date" style="left:84px">28 JANUARY 2018</div>
<div class="abs news-date" style="left:624px">28 JANUARY 2018</div>
<p class="abs news-text" style="left:84px">Lorem Ipsum is simply dummy text of the printing and typesetting industry. Lorem Ipsum has been the industry's standard dummy text ever since the 1500s, when an unknown printer took a galley <b>( More )</b></p>
<p class="abs news-text" style="left:624px">Lorem Ipsum is simply dummy text of the printing and typesetting industry. Lorem Ipsum has been the industry's standard dummy text ever since the 1500s, when an unknown printer took a galley <b>( More )</b></p>

<footer class="abs footer">
  <div class="abs" style="left:72px;top:30px">
    <h4>QUICK LINKS</h4>
    <ul><li>HOME</li><li>ABOUT US</li><li>SERVICES</li><li>NEWS</li><li>TESTIMONIAL</li><li>CONTACT US</li></ul>
  </div>
  <div class="abs fcontact" style="left:426px;top:30px;width:260px">
    <h4>CONTACT US</h4>
    <div><svg width="12" height="14" viewBox="0 0 24 28"><path fill="#fff" d="M12 0a10 10 0 0 0-10 10c0 7.5 10 18 10 18s10-10.5 10-18A10 10 0 0 0 12 0z"/></svg><span>Lorem Ipsum is simply dummy text of the<br>printing and typesetting industry.</span></div>
    <div><svg width="12" height="12" viewBox="0 0 24 24"><path fill="#fff" d="M6.6 10.8a15 15 0 0 0 6.6 6.6l2.2-2.2c.3-.3.7-.4 1-.2 1.1.4 2.3.6 3.6.6.6 0 1 .4 1 1V20c0 .6-.4 1-1 1A17 17 0 0 1 3 4c0-.6.4-1 1-1h3.5c.6 0 1 .4 1 1 0 1.3.2 2.5.6 3.6.1.3 0 .7-.2 1z"/></svg><span>555.014.2290</span></div>
    <div><svg width="12" height="12" viewBox="0 0 24 24"><rect x="2" y="6" width="20" height="14" fill="#fff"/><rect x="6" y="2" width="12" height="6" fill="#fff"/></svg><span>555.014.7731</span></div>
    <div><svg width="12" height="10" viewBox="0 0 24 18"><rect width="24" height="18" fill="#fff"/><path d="m2 3 10 7 10-7" stroke="#333" stroke-width="2" fill="none"/></svg><span>info@qbpane.example</span></div>
  </div>
</footer>
<div class="abs fbrand">Qb Pane</div>
<div class="abs fsocial"><span></span><span></span><span></span><span class="r"></span><span></span></div>
<div class="abs copy">Copyright © 2018 &nbsp;|&nbsp; All Rights Reserved.</div>
<div class="abs totop"><svg width="12" height="8" viewBox="0 0 12 8"><path d="m1 7 5-5 5 5" stroke="#fff" stroke-width="2" fill="none"/></svg></div>

</body>
</html>
```